Menu Design Project

My Restaurant is called The Pita Corner, it's fast food restaurant serves Gyro, Wings, Subs, Fried Seafood and chicken tenders. I'm looking for a menu design to fit the fast food category and have some photos of the food on the front page as well inside the menu. I will attached some photos and you can add any other photo related to the menu from the web.

Industry/Entity Type

Restaurant

```html
<!DOCTYPE html>
<html lang="en">
<head>
<meta charset="utf-8">
<title>The Pita Corner – Menu</title>
<link href="https://fonts.googleapis.com/css2?family=Oswald:wght@400;500;600;700&family=Open+Sans:wght@400;600&family=Arimo:wght@700&display=swap" rel="stylesheet">
<style>
:root{
  --orange-bg:#eeaa36;
  --orange-deep:#e0902a;
  --accent:#e8762a;
  --olive:#7d6c18;
  --maroon:#7a1f1a;
  --lime:#e3e56a;
  --peach:#f3c89e;
  --cream:#f7ecd2;
  --tan:#ead5bb;
  --red:#d4262c;
  --ink:#1e1a16;
}
*{margin:0;padding:0;box-sizing:border-box}
html,body{width:1000px;height:1200px;overflow:hidden;background:#fff}
body{position:relative;font-family:"Open Sans",Arial,sans-serif;color:var(--ink)}
.abs{position:absolute}
.cond{font-family:"Oswald","Arial Narrow",sans-serif}
.panel{position:absolute;width:741px;height:572px;overflow:hidden;
  background:radial-gradient(circle at 60% 40%,#f5be4a 0%,var(--orange-bg) 45%,var(--orange-deep) 100%)}
.front{left:22px;top:18px}
.inside{left:238px;top:608px}
.photo{position:absolute}
/* front */
.headline{position:absolute;font-family:"Oswald",sans-serif;font-weight:600;line-height:1;text-transform:uppercase;letter-spacing:-1px}
.drinks{left:33px;top:252px;width:307px;height:62px;background:rgba(226,232,78,.85);border:1.5px solid var(--maroon);text-align:center}
.drinks h2{font-family:"Oswald",sans-serif;font-weight:600;color:var(--olive);font-size:24px;line-height:30px}
.drinks p{font-size:9.5px;line-height:12px}
.callout{left:33px;top:350px;width:145px;color:var(--maroon);font-family:"Oswald",sans-serif;font-size:15.5px;font-weight:600;line-height:22px;text-transform:uppercase;white-space:nowrap}
.hours h3{font-family:"Oswald",sans-serif;color:var(--olive);font-size:26px;font-weight:600}
.hours p{color:var(--maroon);font-size:11px;font-weight:600;font-family:"Oswald",sans-serif}
.like{left:33px;top:526px;color:var(--maroon);font-family:"Oswald",sans-serif;font-size:10px;display:flex;align-items:center;gap:4px}
.like span.sq{width:9px;height:9px;background:var(--red);display:inline-block}
.map-addr{left:181px;top:512px;width:160px;text-align:center;color:var(--maroon);font-family:"Oswald",sans-serif;font-size:11.5px;line-height:17px}
.brand{left:420px;top:195px;width:300px;display:flex;align-items:center;justify-content:center;gap:10px}
.brand .dot{width:22px;height:22px;border-radius:50%;background:var(--red)}
.brand h1{font-family:"Arimo",Arial,sans-serif;font-size:32px;font-weight:700;color:#000;white-space:nowrap}
.contact{left:420px;top:262px;width:300px;text-align:center;color:var(--maroon);font-family:"Oswald",sans-serif}
/* inside */
.sheet{left:34px;top:32px;width:673px;height:520px;background:var(--cream)}
.box{position:absolute;border:1.3px solid var(--maroon)}
.title{font-family:"Oswald",sans-serif;font-weight:600;color:var(--olive);text-transform:uppercase;line-height:1;white-space:nowrap}
.list{list-style:none;font-size:10px;line-height:17px}
.list b{font-family:"Oswald",sans-serif;font-weight:500;color:var(--accent);text-transform:uppercase;font-size:10.5px}
.subs{display:grid;grid-template-columns:122px 36px 36px;font-size:10px;line-height:17px;white-space:nowrap}
.subs b{font-family:"Oswald",sans-serif;font-weight:500;color:var(--accent);font-size:10.5px}
.subs small{font-size:8.5px}
</style>
</head>
<body>

<section class="panel front">
  <div class="photo" role="img" aria-label="Photo of an iced cola in a tall glass" style="left:0;top:72px;width:140px;height:268px;background:linear-gradient(180deg,#d9c8a8,#7a2c12 30%,#5a1a08 80%,#c9a98a)"></div>

  <div class="headline" style="left:35px;top:30px;font-size:54px;color:var(--olive)">Good Food,</div>
  <div class="headline" style="left:172px;top:82px;font-size:62px;color:var(--accent)">Good</div>
  <div class="headline" style="left:200px;top:148px;font-size:72px;color:var(--accent)">Mood</div>

  <div class="abs drinks">
    <h2>DRINKS</h2>
    <p>Cola, Diet Cola, Lemon-Lime Soda, Sports Drink, Orange Soda,<br>Strawberry Soda, Cherry Pop and more.</p>
  </div>

  <div class="abs callout">Call us for pick up<br>orders or catering<br>@ 713-555-0182</div>

  <div class="photo" role="img" aria-label="Street map showing the restaurant location" style="left:181px;top:352px;width:160px;height:152px;background:linear-gradient(135deg,#eceae4,#dcdad2);border:1.5px solid var(--maroon)"></div>
  <div class="abs map-addr">4120 HARBOR VIEW BLVD,<br>HOUSTON, TX 77045</div>

  <div class="abs hours" style="left:33px;top:458px">
    <h3>HOURS.</h3>
    <p>MONDAY TO SUNDAY &nbsp;11AM-9PM</p>
  </div>
  <div class="abs like">LIKE US <span class="sq"></span></div>

  <div class="abs brand"><span class="dot"></span><h1>The Pita Corner</h1></div>
  <div class="abs contact">
    <p style="font-size:11px">4120 Harbor View Blvd, Houston, TX 77045</p>
    <p style="font-size:16px;font-weight:600;line-height:24px">713-555-0182</p>
    <p style="font-size:11px">Hours: Monday to Sunday 11am-9pm</p>
  </div>

  <div class="photo" role="img" aria-label="Photo of a gyro wrap with meat, lettuce and tomato" style="left:450px;top:338px;width:291px;height:234px;border-radius:60px 0 0 20px;background:linear-gradient(135deg,#f2ede4,#7a4a2a 40%,#5a3018 70%,#e8d6b8)"></div>
</section>

<section class="panel inside">
  <div class="abs sheet"></div>
  <div class="photo" role="img" aria-label="Photo of a ripe red tomato" style="left:0;top:40px;width:66px;height:120px;border-radius:0 60px 60px 0;background:radial-gradient(circle at 40% 40%,#f0452e,#b81810)"></div>

  <div class="abs" style="left:52px;top:46px;width:160px;text-align:center">
    <div class="title" style="font-size:26px"><span style="font-weight:400">FRESH</span> SALADS</div>
    <ul class="list" style="margin-top:4px;line-height:15.5px">
      <li><b>Caesar Salad</b> $4.95</li>
      <li><b>Gyro Salad</b> $5.95</li>
      <li><b>Shrimp Caesar Salad</b> $6.25</li>
      <li><b>Greek Salad</b> $5.95</li>
    </ul>
  </div>

  <div class="box" style="left:49px;top:181px;width:157px;height:344px;background:var(--peach)">
    <div class="title" style="font-size:28px;text-align:center;margin-top:20px">CHICKEN</div>
    <ul class="list" style="margin:14px 0 0 15px">
      <li><b>10 Large Wings</b> $8.99</li>
      <li><b>20 Large Wings</b> $16.99</li>
      <li style="margin-top:10px"><b>30 Large Wings</b> $23.99</li>
      <li><b>50 Large Wings</b> $39.99</li>
      <li style="margin-top:10px">½ lb. <b>Chicken Strips</b> $5.49</li>
      <li>1lb. <b>Chicken Strips</b> $7.99</li>
      <li style="margin-top:10px">½ lb. <b>Gizzards</b> $5.49</li>
      <li>1lb. <b>Gizzards</b> $7.99</li>
    </ul>
    <div class="photo" role="img" aria-label="Photo of fried chicken wings" style="left:0;bottom:0;width:155px;height:100px;background:linear-gradient(160deg,#6a9a3a 0%,#d8742a 35%,#a8401a 100%)"></div>
  </div>

  <div class="box" style="left:235px;top:49px;width:123px;height:135px;background:var(--lime);text-align:center">
    <div class="title" style="font-size:28px;margin-top:6px">SEAFOOD</div>
    <ul class="list" style="margin-top:6px;line-height:16.5px">
      <li>½ lb. <b>Shrimp</b> $7.99</li>
      <li>1lb. <b>Shrimp</b> $13.99</li>
      <li>½ lb. <b>Fish</b> $6.99</li>
      <li>1lb. <b>Fish</b> $12.99</li>
    </ul>
  </div>

  <div class="abs" style="left:237px;top:204px">
    <div class="title" style="font-size:28px;margin-left:30px">SIDES</div>
    <ul class="list" style="margin-top:8px">
      <li><b>French Fries</b> $2.79</li>
      <li><b>Cajun Fries</b> $3.99</li>
      <li><b>Onion Rings</b> $4.99</li>
      <li><b>5 Jalapeno Poppers</b> $4.99</li>
      <li><b>Fried Okra</b> $4.99</li>
      <li><b>Fried Mushroom</b> $5.49</li>
      <li><b>5 Mozzarella Sticks</b> $5.49</li>
    </ul>
  </div>

  <div class="box" style="left:229px;top:375px;width:124px;height:150px;background:var(--lime)">
    <div class="title" style="font-size:24px;text-align:center;margin-top:12px">KIDS <span style="font-weight:400">MEAL</span></div>
    <ul class="list" style="margin:6px 0 0 5px;line-height:13px;font-size:9.5px">
      <li><b>Chicken Nuggets</b> 4pc with small drink and fries $4.95</li>
      <li style="margin-top:3px"><b>Chicken Strips</b> 2pc with small drink and fries $4.95</li>
      <li style="margin-top:3px"><b>Mac &amp; Cheese</b> $3.95</li>
    </ul>
  </div>

  <div class="box" style="left:390px;top:49px;width:300px;height:200px;background:var(--lime);text-align:center">
    <div class="title" style="font-size:28px;margin-top:5px;margin-left:-30px">COMBOS</div>
    <div class="abs cond" style="right:10px;top:8px;font-size:10.5px;color:var(--maroon);line-height:16px">INCLUDES 16OZ<br>SOFT DRINK!</div>
    <ul class="list" style="margin-top:4px;line-height:15.5px">
      <li>½ lb. <b>Fish &amp; Fries</b> $9.99</li>
      <li>½ lb. <b>Shrimp &amp; Fries</b> $10.99</li>
      <li>6" <b>Philly</b> (Steak or Chicken) <b>&amp; Fries</b> $9.99</li>
      <li><b>Gyro</b> (Original, Chicken or Fish) <b>&amp; Fries</b> $9.49</li>
      <li>5 <b>Wings &amp; Fries</b> $9.49</li>
      <li>½ lb. <b>Gizzards &amp; Fries</b> $7.99</li>
      <li style="line-height:12px">¼ lb. <b>Burger &amp; Fries</b> $6.99<br>*CHEESE EXTRA</li>
      <li>5 <b>Wings &amp; Gizzards</b> $11.49</li>
      <li>½ lb. <b>Chicken Strips &amp; Fries</b> $7.99</li>
    </ul>
  </div>

  <div class="box" style="left:390px;top:264px;width:300px;height:260px;background:var(--tan)">
    <div class="title" style="font-size:28px;text-align:center;margin-top:10px;margin-left:-50px">GYROS &amp; SUBS</div>
    <ul class="list" style="margin:8px 0 0 7px">
      <li><b>Gyro</b> (Original or Chicken) $6.99</li>
      <li>¼ lb. <b>Burger</b> $3.99</li>
      <li><b>Buffalo Chicken Sandwich</b> $5.99</li>
    </ul>
    <div class="cond" style="margin:32px 0 2px 7px;font-size:9.5px;font-weight:500;color:var(--maroon);white-space:nowrap">YOUR CHOICE OF 6" OR FOOTLONG SUBS</div>
    <div class="subs" style="margin-left:7px">
      <span><b>PHILLY</b> <small>(Steak or Chicken)</small></span><span>$6.75</span><span>$8.99</span>
      <span><b>PO BOY SHRIMP</b></span><span>$7.55</span><span>$9.25</span>
      <span><b>FISH</b></span><span>$6.75</span><span>$8.99</span>
      <span><b>TURKEY &amp; CHEESE</b></span><span>$6.49</span><span>$7.95</span>
    </div>
  </div>

  <div class="photo" role="img" aria-label="Photo of a cheeseburger with lettuce and tomato" style="left:603px;top:302px;width:138px;height:270px;border-radius:70px 0 0 30px;background:linear-gradient(180deg,#e0a050 0%,#c87830 25%,#5fa030 40%,#d8302a 52%,#4a2a18 68%,#d89a48 88%)"></div>
</section>

</body>
</html>
```